"Cork Hollow Excursions" is a top notch Santa Barbara County Wine Tour company.

We provide scenic, boutique and custom wine tours. I need the card to be clean and classy. I will provide our logo. I would like the logo to cover the back side of the card as an option and would like to see a couple color options other then our signature green and gold. I would like to see some creative options and let the designers come up with options.
I need cards for myself and my team. The final design should communicate "An authentic and boutique wine tour experience"
Please use my website for reference www.corkhollowexcursions.com

Target Market(s)

We have a wide range of clients from millennials to baby boomers

Industry/Entity Type

Tour

Contact Information for Business Card

Contact info:
Dale Munford
805-291-6384
info@corkhollowexcursions.com
corkhollowexcursions.com

Colors

Designer to choose colors to be used in the design.

Requirements
Must have
• my logo
Nice to have
• *I would like to have the backside side with the logo and the company statement
• "An authentic and boutique wine tour experience" as an option.
• *I would also like to see what the designers can create!
• *I would like to see an option that incorporates or social: snapgrid, rovia, route scout
Should not have
• I do not want it too busy.

```html
<!DOCTYPE html>
<html lang="en">
<head>
<meta charset="utf-8">
<title>Cork Hollow Excursions – Business Card</title>
<link rel="stylesheet" href="https://fonts.googleapis.com/css2?family=Open+Sans:wght@400;600&display=swap">
<style>
  :root {
    --page: #e9e6e2;
    --card: #141516;
    --green: #2f6b3f;
    --green-bright: #3f8a52;
    --gold: #c9b08c;
    --ink: #f2f2f2;
    --muted: #b9b9b9;
    --social-a: #8a7a62;
    --social-b: #4f8a3c;
    --social-c: #c6362c;
  }
  * { box-sizing: border-box; margin: 0; padding: 0; }
  html, body { width: 1200px; height: 864px; overflow: hidden; }
  body {
    background: var(--page);
    font-family: "Open Sans", sans-serif;
    display: flex;
    align-items: center;
    justify-content: center;
    gap: 40px;
  }
  .card {
    position: relative;
    width: 540px;
    height: 309px;
    background: var(--card);
    border-radius: 3px;
    box-shadow: 0 10px 30px rgba(0,0,0,0.25);
    overflow: hidden;
  }

  /* Back side: logo + statement */
  .brand-mark {
    position: absolute;
    left: 0; right: 0; top: 96px;
    text-align: center;
    color: var(--green-bright);
    font-weight: 600;
    font-size: 30px;
    letter-spacing: 0.5px;
  }
  .statement {
    position: absolute;
    left: 0; right: 0; top: 196px;
    text-align: center;
    color: var(--muted);
    font-size: 15px;
  }
  .social {
    position: absolute;
    top: 22px; right: 22px;
    display: flex;
    flex-direction: column;
    align-items: flex-end;
    gap: 6px;
  }
  .social-item {
    display: flex;
    align-items: center;
    gap: 6px;
    color: var(--muted);
    font-size: 11px;
  }
  .social-item .chip { width: 14px; height: 14px; border-radius: 3px; }
  .chip.snapgrid { background: var(--social-a); }
  .chip.route-scout { background: var(--social-b); }
  .chip.rovia { background: var(--social-c); }

  /* Front side: contact */
  .contact {
    position: absolute;
    left: 34px; top: 120px;
  }
  .person-name {
    color: var(--green-bright);
    font-weight: 600;
    font-size: 19px;
    letter-spacing: 0.3px;
    padding-bottom: 6px;
  }
  .name-rule {
    position: absolute;
    left: 34px; top: 152px;
    width: 232px; height: 1px;
    background: var(--ink);
  }
  .contact-list {
    list-style: none;
    margin-top: 14px;
  }
  .contact-list li {
    display: flex;
    align-items: center;
    gap: 10px;
    color: var(--ink);
    font-size: 14px;
    line-height: 22px;
  }
  .contact-list svg { width: 12px; height: 12px; fill: var(--green-bright); flex: none; }
  .company-lockup {
    position: absolute;
    right: 30px; top: 104px;
    width: 230px;
    text-align: center;
    color: var(--gold);
    font-weight: 600;
    font-size: 22px;
    line-height: 1.25;
  }
  .base-rule {
    position: absolute;
    left: 34px; right: 34px; top: 262px;
    height: 1px;
    background: var(--ink);
  }
</style>
</head>
<body>

  <section class="card card-back" aria-label="Card back">
    <div class="social">
      <span class="social-item">snapgrid <span class="chip snapgrid"></span></span>
      <span class="social-item">route scout <span class="chip route-scout"></span></span>
      <span class="social-item">rovia <span class="chip rovia"></span></span>
    </div>
    <div class="brand-mark">Cork Hollow Excursions</div>
    <p class="statement">An authentic &amp; boutique wine tour experience</p>
  </section>

  <section class="card card-front" aria-label="Card front">
    <div class="contact">
      <h1 class="person-name">DALE MUNFORD</h1>
      <ul class="contact-list">
        <li>
          <svg viewBox="0 0 24 24" aria-hidden="true"><path d="M6.6 10.8a15.1 15.1 0 0 0 6.6 6.6l2.2-2.2a1 1 0 0 1 1-.25 11.4 11.4 0 0 0 3.6.57 1 1 0 0 1 1 1V20a1 1 0 0 1-1 1A17 17 0 0 1 3 4a1 1 0 0 1 1-1h3.5a1 1 0 0 1 1 1c0 1.25.2 2.45.57 3.57a1 1 0 0 1-.25 1z"/></svg>
          805-291-6384
        </li>
        <li>
          <svg viewBox="0 0 24 24" aria-hidden="true"><path d="M2 5h20v2l-10 6L2 7zm0 4.3 10 6 10-6V19H2z"/></svg>
          info@corkhollowexcursions.com
        </li>
        <li>
          <svg viewBox="0 0 24 24" aria-hidden="true"><circle cx="12" cy="12" r="10"/></svg>
          corkhollowexcursions.com
        </li>
      </ul>
    </div>
    <div class="name-rule"></div>
    <div class="company-lockup">Cork Hollow Excursions</div>
    <div class="base-rule"></div>
  </section>

</body>
</html>
```